Web Design for Financial Consulting Company

We need a website design for a financial consulting company "Korvane Consulting". We build financial models, scenario analysis, handle the budgeting process and provide temporary staffing. I have over 10 years of experience. My Excel expertise and analytical savvy has saved clients over $17 million in profit.

Target Market(s)

Small to medium businesses

Industry/Entity Type

Financial Consulting

Number of Pages Required

4 page

Requirements
Must have
• Professional looking
Nice to have
• A little futuristic looking

```html
<!DOCTYPE html>
<html lang="en">
<head>
<meta charset="utf-8">
<title>Korvane Consulting</title>
<link href="https://fonts.googleapis.com/css2?family=Poppins:wght@400;500;600;700&display=swap" rel="stylesheet">
<style>
:root{
  --blue:#0d9ee8;
  --blue-deep:#0a6fb3;
  --navy:#0a3a5c;
  --footer:#0b3455;
  --ink:#1f1f1f;
  --text:#555b63;
  --muted:#7a8088;
  --pale:#f2f9fd;
  --star:#f5b400;
  --line:#d4d8dd;
}
*{box-sizing:border-box;margin:0;padding:0}
html,body{width:1200px;height:2898px;overflow:hidden}
body{position:relative;font-family:'Poppins',sans-serif;color:var(--ink);background:#fff}
.abs{position:absolute}
.btn{position:absolute;display:flex;align-items:center;justify-content:center;background:var(--blue);color:#fff;font-weight:600;font-size:14px;border-radius:4px}

/* header */
.header{left:0;top:0;width:1200px;height:68px;background:#fff;z-index:3}
.brand{display:flex;align-items:center;gap:10px;color:var(--navy);font-weight:600;font-size:24px;letter-spacing:.5px}
.brand-mark{width:30px;height:30px;border:3px solid var(--blue)}
.nav a{position:absolute;top:26px;font-size:13px;color:#444;text-decoration:none}
.nav a.active{font-weight:600;color:var(--ink)}
.nav-underline{left:534px;top:66px;width:39px;height:2px;background:var(--blue)}

/* hero */
.hero{left:0;top:68px;width:1200px;height:505px;background:linear-gradient(90deg,#eef1f3 0%,#e6eaed 45%,#d7dde2 100%)}
.hero-photo{left:480px;top:68px;width:720px;height:505px;background:linear-gradient(100deg,rgba(230,234,237,0) 0%,#c9cfd5 30%,#a9b0b8 60%,#e6a26b 85%,#f0c49b 100%)}
.hero-title{left:111px;top:164px;width:520px;font-size:50px;line-height:56px;font-weight:600;color:var(--ink)}
.hero-lead{left:112px;top:348px;width:440px;font-size:16px;line-height:22px;color:#333}
.stat{top:533px;height:80px;width:414px;background:#fff;border-radius:4px;box-shadow:0 8px 24px rgba(0,0,0,.08);display:flex;align-items:center;gap:16px;padding-left:44px;font-size:14px;font-weight:600;line-height:17px}

/* about */
.about-photo{left:112px;top:675px;width:348px;height:378px;border-radius:4px;background:linear-gradient(135deg,#3a4a5e,#6b7a8a 50%,#2d5fa8)}
.play{left:413px;top:921px;width:94px;height:94px;border-radius:50%;background:#fff;box-shadow:0 6px 24px rgba(0,0,0,.12);display:flex;align-items:center;justify-content:center}
.eyebrow{font-size:13px;font-weight:600;color:var(--blue)}
.h2{font-size:33px;line-height:38px;font-weight:600;color:var(--ink)}
.about-text{left:591px;top:801px;width:480px;font-size:11.5px;line-height:19px;color:var(--text)}
.bullets{list-style:none}
.bullets li{position:relative;padding-left:28px;font-size:13px;color:#333;height:33.5px}
.bullets li::before{content:"";position:absolute;left:0;top:3px;width:15px;height:15px;border-radius:50%;background:var(--navy)}

/* services */
.services{left:0;top:1128px;width:1200px;height:540px;background:var(--pale)}
.card{top:1336px;width:233px;height:271px;background:#fff;border-radius:8px;box-shadow:0 6px 20px rgba(0,60,110,.06);text-align:center}
.card .ic{width:84px;height:84px;border-radius:50%;background:#fff;box-shadow:0 4px 16px rgba(0,0,0,.08);margin:34px auto 0;display:flex;align-items:center;justify-content:center}
.card h3{font-size:16px;font-weight:600;margin-top:26px}
.card p{font-size:11.5px;line-height:19px;color:var(--muted);margin:12px auto 0;width:190px}

/* testimonials */
.testi{left:0;top:1668px;width:1200px;height:520px;background:linear-gradient(120deg,#16aef5 0%,#0c95e0 55%,#0a6fb3 100%)}
.tcard{top:1828px;width:442px;height:248px;background:#fff;border-radius:6px}
.avatar{position:absolute;left:38px;top:28px;width:80px;height:80px;border-radius:50%;border:2px solid var(--navy);padding:3px}
.avatar span{display:block;width:100%;height:100%;border-radius:50%;background:linear-gradient(160deg,#b7c2cc,#6e7a86)}
.tname{position:absolute;left:145px;top:42px;font-size:16px;font-weight:600}
.trole{position:absolute;left:145px;top:64px;font-size:13px;color:var(--blue)}
.stars{position:absolute;left:145px;top:86px;display:flex;gap:6px}
.quote{position:absolute;right:46px;top:34px}
.tbody{position:absolute;left:53px;top:128px;width:340px;font-size:12.5px;line-height:19px;color:var(--text)}
.dot{top:2112px;width:11px;height:11px;border-radius:50%;background:rgba(255,255,255,.55)}

/* contact */
.contact-text{left:112px;top:2364px;width:500px;font-size:13px;line-height:19px;color:var(--text)}
.phone-badge{left:112px;top:2572px;width:50px;height:50px;border-radius:50%;background:var(--blue);display:flex;align-items:center;justify-content:center}
.form-card{left:694px;top:2238px;width:394px;height:394px;background:#fff;border-radius:8px;box-shadow:0 8px 30px rgba(0,0,0,.07)}
.field{position:absolute;width:162px;height:40px;border:1px solid var(--line);border-radius:3px;font-size:10.5px;color:#8a9097;display:flex;align-items:center;padding-left:18px}
.field svg{position:absolute;right:14px;top:16px}

/* footer */
.footer{left:0;top:2673px;width:1200px;height:225px;background:var(--footer)}
.foot-rule{top:2782px;height:1px;background:rgba(255,255,255,.35)}
.social{top:2766px;width:34px;height:34px;border-radius:3px;background:#fff}
.foot-nav a{position:absolute;top:2820px;font-size:12px;color:#fff;text-decoration:none}
.copy{left:0;top:2866px;width:1200px;text-align:center;font-size:10px;color:#fff}
</style>
</head>
<body>

<!-- Header -->
<header class="abs header">
  <div class="abs brand" style="left:112px;top:20px"><span class="brand-mark"></span>Korvane Consulting</div>
  <nav class="nav">
    <a class="active" style="left:537px">Home</a>
    <a style="left:602px">About</a>
    <a style="left:672px">Service</a>
    <a style="left:751px">Contact</a>
  </nav>
  <div class="abs nav-underline"></div>
  <svg class="abs" style="left:852px;top:28px" width="22" height="22" viewBox="0 0 22 22"><circle cx="9" cy="9" r="7" fill="none" stroke="#333" stroke-width="1.6"/><line x1="14" y1="14" x2="20" y2="20" stroke="#333" stroke-width="2"/></svg>
  <div class="btn" style="left:916px;top:18px;width:172px;height:42px">Request &amp; Call</div>
</header>

<!-- Hero -->
<section class="abs hero"></section>
<div class="abs hero-photo" role="img" aria-label="Businesswoman with tablet blended over a sunlit city skyline"></div>
<h1 class="abs hero-title">Helping your<br>finance team and<br>increasing profit</h1>
<p class="abs hero-lead">Lorem ipsum dolor sit amet, consectetur adipiscing elit, sed do eiusmod tempor incididunt ut labore et dolore magna aliqua.</p>

<div class="abs stat" style="left:176px">
  <svg width="36" height="40" viewBox="0 0 36 40"><path d="M18 2a14 14 0 0 0-14 14c0 5 3 8 5 10v12h14v-6h6a3 3 0 0 0 3-3v-5l4-1-4-8A14 14 0 0 0 18 2z" fill="var(--blue)"/><circle cx="17" cy="15" r="5" fill="#fff"/></svg>
  Over 10 years of experience
</div>
<div class="abs stat" style="left:610px;padding-left:44px">
  <svg width="38" height="40" viewBox="0 0 38 40"><circle cx="22" cy="11" r="9" fill="var(--blue)"/><text x="22" y="15" font-size="12" fill="#fff" text-anchor="middle" font-family="Poppins,sans-serif" font-weight="700">$</text><path d="M2 26h8l8 3h8a3 3 0 0 1 0 6H14v1h14l8-6v6l-8 4H2z" fill="var(--blue)"/></svg>
  <span>I have successfully increased<br>profitability for clients by $17M.</span>
</div>

<!-- About -->
<div class="abs about-photo" role="img" aria-label="Team of consultants reviewing work on a laptop"></div>
<div class="abs play"><svg width="28" height="32" viewBox="0 0 28 32"><path d="M2 2l24 14L2 30z" fill="var(--blue)"/></svg></div>
<div class="abs eyebrow" style="left:591px;top:682px">About Our Company</div>
<h2 class="abs h2" style="left:590px;top:711px;width:420px">Read The Story Behind Our Success</h2>
<p class="abs about-text">I am an experienced Finance professional who develops strategic financial plans, provides insightful analysis, and supports decision-making. With over 10 years of experience, I have successfully increased profitability<br>for clients by $17M.</p>
<ul class="abs bullets" style="left:591px;top:892px">
  <li>Premium services and beyond your expectation</li>
  <li>Get the best support among all venders</li>
  <li>Fully responsive and works great on all major devices</li>
</ul>
<div class="btn" style="left:591px;top:997px;width:172px;height:49px">More About Us</div>

<!-- Services -->
<section class="abs services"></section>
<div class="abs eyebrow" style="left:112px;top:1188px">Our Service</div>
<h2 class="abs h2" style="left:112px;top:1216px;width:500px">We run all kinds of service that your success</h2>
<div class="btn" style="left:916px;top:1229px;width:172px;height:49px">View More</div>

<div class="abs card" style="left:112px">
  <div class="ic"><svg width="42" height="42" viewBox="0 0 42 42"><g stroke="var(--blue)" stroke-width="3"><line x1="8" y1="8" x2="34" y2="34"/><line x1="34" y1="8" x2="8" y2="34"/></g><circle cx="21" cy="21" r="10" fill="var(--blue)"/><circle cx="7" cy="7" r="4" fill="var(--navy)"/><circle cx="35" cy="7" r="4" fill="var(--navy)"/><circle cx="7" cy="35" r="4" fill="var(--navy)"/><circle cx="35" cy="35" r="4" fill="var(--navy)"/><text x="21" y="26" font-size="13" fill="#fff" text-anchor="middle" font-family="Poppins,sans-serif" font-weight="700">$</text></svg></div>
  <h3>Financial Models</h3>
  <p>Financial analysis, scenario modeling, pricing analysis, projects</p>
</div>
<div class="abs card" style="left:360px">
  <div class="ic"><svg width="42" height="42" viewBox="0 0 42 42"><circle cx="21" cy="21" r="17" fill="none" stroke="var(--blue)" stroke-width="2.5" stroke-dasharray="20 6"/><circle cx="21" cy="21" r="9" fill="var(--navy)"/><text x="21" y="25" font-size="11" fill="#fff" text-anchor="middle" font-family="Poppins,sans-serif" font-weight="700">$</text></svg></div>
  <h3>Budgeting Process</h3>
  <p>Building budgets from scratch, revamping current process to be more robust and scalable.</p>
</div>
<div class="abs card" style="left:607px">
  <div class="ic"><svg width="42" height="34" viewBox="0 0 42 34"><circle cx="21" cy="8" r="6" fill="var(--blue)"/><circle cx="8" cy="11" r="5" fill="var(--blue)"/><circle cx="34" cy="11" r="5" fill="var(--blue)"/><rect x="13" y="16" width="16" height="16" rx="4" fill="var(--blue)"/><rect x="1" y="18" width="13" height="13" rx="4" fill="var(--blue)"/><rect x="28" y="18" width="13" height="13" rx="4" fill="var(--blue)"/></svg></div>
  <h3>Temporary Staffing</h3>
  <p>Years of Financial Planning and Analysis experience across multiple industries can help temporary staffing needs.</p>
</div>
<div class="abs card" style="left:855px">
  <div class="ic"><svg width="42" height="42" viewBox="0 0 42 42"><circle cx="21" cy="21" r="15" fill="none" stroke="var(--blue)" stroke-width="7" stroke-dasharray="6 3.5"/><circle cx="21" cy="21" r="11" fill="var(--blue)"/><path d="M21 13l7 8h-4v7h-6v-7h-4z" fill="#fff"/></svg></div>
  <h3>Process Improvement</h3>
  <p style="width:170px">Month end close, reporting, budg</p>
</div>

<!-- Testimonials -->
<section class="abs testi"></section>
<div class="abs" style="left:0;top:1722px;width:1200px;text-align:center;font-size:13px;font-weight:600;color:var(--navy)">Testimonial</div>
<h2 class="abs" style="left:0;top:1750px;width:1200px;text-align:center;font-size:31px;font-weight:600;color:#fff">What Our Happy Clients Say?</h2>

<div class="abs tcard" style="left:149px">
  <div class="avatar"><span role="img" aria-label="Portrait of client"></span></div>
  <div class="tname">Tomas Reyland</div>
  <div class="trole">Co- Of Officer</div>
  <div class="stars">
    <svg width="17" height="16" viewBox="0 0 24 23"><path d="M12 0l3.6 7.6 8.4 1-6.2 5.8 1.6 8.3L12 18.6 4.6 22.7l1.6-8.3L0 8.6l8.4-1z" fill="var(--star)"/></svg>
    <svg width="17" height="16" viewBox="0 0 24 23"><path d="M12 0l3.6 7.6 8.4 1-6.2 5.8 1.6 8.3L12 18.6 4.6 22.7l1.6-8.3L0 8.6l8.4-1z" fill="var(--star)"/></svg>
    <svg width="17" height="16" viewBox="0 0 24 23"><path d="M12 0l3.6 7.6 8.4 1-6.2 5.8 1.6 8.3L12 18.6 4.6 22.7l1.6-8.3L0 8.6l8.4-1z" fill="var(--star)"/></svg>
    <svg width="17" height="16" viewBox="0 0 24 23"><path d="M12 0l3.6 7.6 8.4 1-6.2 5.8 1.6 8.3L12 18.6 4.6 22.7l1.6-8.3L0 8.6l8.4-1z" fill="var(--star)"/></svg>
    <svg width="17" height="16" viewBox="0 0 24 23"><path d="M12 0l3.6 7.6 8.4 1-6.2 5.8 1.6 8.3L12 18.6 4.6 22.7l1.6-8.3L0 8.6l8.4-1z" fill="var(--star)"/></svg>
  </div>
  <svg class="quote" width="70" height="60" viewBox="0 0 70 60"><path d="M0 0h30v36L18 60H6l8-24H0zM40 0h30v36L58 60H46l8-24H40z" fill="#d3d3d3"/></svg>
  <p class="tbody">Lorem ipsum dolor sit amet, consectetur adipiscing elit, sed do eiusmod tempor incididunt ut labore et dolore magna aliqua. Quis ipsum suspendisse ultrices gravida. Risus commodo viverra maecenas accumsan lacus vel facilisis.</p>
</div>
<div class="abs tcard" style="left:610px">
  <div class="avatar"><span role="img" aria-label="Portrait of client" style="background:linear-gradient(160deg,#9a7b66,#4f3d33)"></span></div>
  <div class="tname">Elena Varga</div>
  <div class="trole">Manager</div>
  <div class="stars">
    <svg width="17" height="16" viewBox="0 0 24 23"><path d="M12 0l3.6 7.6 8.4 1-6.2 5.8 1.6 8.3L12 18.6 4.6 22.7l1.6-8.3L0 8.6l8.4-1z" fill="var(--star)"/></svg>
    <svg width="17" height="16" viewBox="0 0 24 23"><path d="M12 0l3.6 7.6 8.4 1-6.2 5.8 1.6 8.3L12 18.6 4.6 22.7l1.6-8.3L0 8.6l8.4-1z" fill="var(--star)"/></svg>
    <svg width="17" height="16" viewBox="0 0 24 23"><path d="M12 0l3.6 7.6 8.4 1-6.2 5.8 1.6 8.3L12 18.6 4.6 22.7l1.6-8.3L0 8.6l8.4-1z" fill="var(--star)"/></svg>
    <svg width="17" height="16" viewBox="0 0 24 23"><path d="M12 0l3.6 7.6 8.4 1-6.2 5.8 1.6 8.3L12 18.6 4.6 22.7l1.6-8.3L0 8.6l8.4-1z" fill="var(--star)"/></svg>
    <svg width="17" height="16" viewBox="0 0 24 23"><path d="M12 0l3.6 7.6 8.4 1-6.2 5.8 1.6 8.3L12 18.6 4.6 22.7l1.6-8.3L0 8.6l8.4-1z" fill="var(--star)"/></svg>
  </div>
  <svg class="quote" width="70" height="60" viewBox="0 0 70 60"><path d="M0 0h30v36L18 60H6l8-24H0zM40 0h30v36L58 60H46l8-24H40z" fill="#d3d3d3"/></svg>
  <p class="tbody">Lorem ipsum dolor sit amet, consectetur adipiscing elit, sed do eiusmod tempor incididunt ut labore et dolore magna aliqua. Quis ipsum suspendisse ultrices gravida. Risus commodo viverra maecenas accumsan lacus vel facilisis.</p>
</div>
<div class="abs dot" style="left:571px;background:#fff"></div>
<div class="abs dot" style="left:594px"></div>
<div class="abs dot" style="left:618px"></div>

<!-- Contact -->
<div class="abs eyebrow" style="left:112px;top:2243px">Get In Touch</div>
<h2 class="abs h2" style="left:112px;top:2271px;width:330px">What We Can Help For You</h2>
<p class="abs contact-text">Lorem ipsum dolor sit amet, consectetur adipiscing elit. Curabitur commodo eleifend hendrerit. Vivamus sodales, sem et accumsan fermentum, erat enim dignissim risus, et convallis erat nisl ut mauris.</p>
<ul class="abs bullets" style="left:112px;top:2443px">
  <li>48 Harbor Row, Westfield, NY</li>
  <li>Which don't Look Even Slightly Believable</li>
  <li>000 555 0142 318</li>
</ul>
<div class="abs phone-badge"><svg width="20" height="20" viewBox="0 0 24 24"><path d="M6.6 10.8a15 15 0 0 0 6.6 6.6l2.2-2.2a1 1 0 0 1 1-.25 11 11 0 0 0 3.6.6 1 1 0 0 1 1 1V20a1 1 0 0 1-1 1A17 17 0 0 1 3 4a1 1 0 0 1 1-1h3.5a1 1 0 0 1 1 1 11 11 0 0 0 .6 3.6 1 1 0 0 1-.25 1z" fill="#fff"/></svg></div>
<div class="abs" style="left:183px;top:2557px;font-size:13px;font-weight:600">Quick Support Number</div>
<div class="abs" style="left:183px;top:2578px;font-size:17px;font-weight:600;color:var(--blue)">(+00 5550 1427 93)</div>

<div class="abs form-card">
  <div class="abs eyebrow" style="left:29px;top:46px">Contact Us</div>
  <div class="abs" style="left:28px;top:68px;font-size:31px;font-weight:600">Request A Quote</div>
  <div class="field" style="left:29px;top:118px">Name</div>
  <div class="field" style="left:203px;top:118px">Eamil</div>
  <div class="field" style="left:29px;top:170px">Select Company<svg width="9" height="6" viewBox="0 0 9 6"><path d="M1 1l3.5 3.5L8 1" fill="none" stroke="#888"/></svg></div>
  <div class="field" style="left:203px;top:170px">Select Staircase<svg width="9" height="6" viewBox="0 0 9 6"><path d="M1 1l3.5 3.5L8 1" fill="none" stroke="#888"/></svg></div>
  <div class="field" style="left:29px;top:221px">Phone</div>
  <div class="field" style="left:203px;top:221px">Room Select<svg width="9" height="6" viewBox="0 0 9 6"><path d="M1 1l3.5 3.5L8 1" fill="none" stroke="#888"/></svg></div>
  <div class="btn" style="left:30px;top:281px;width:172px;height:50px">Send Message</div>
</div>

<!-- Footer -->
<footer class="abs footer"></footer>
<div class="abs brand" style="left:0;top:2700px;width:1200px;justify-content:center;color:#fff"><span class="brand-mark"></span>Korvane Consulting</div>
<div class="abs foot-rule" style="left:0;width:496px"></div>
<div class="abs foot-rule" style="left:704px;width:496px"></div>
<div class="abs social" style="left:513px" aria-label="Social link 1"></div>
<div class="abs social" style="left:560px" aria-label="Social link 2"></div>
<div class="abs social" style="left:606px" aria-label="Social link 3"></div>
<div class="abs social" style="left:652px" aria-label="Social link 4"></div>
<nav class="foot-nav">
  <a style="left:469px;font-weight:600">Home</a>
  <a style="left:534px">About</a>
  <a style="left:604px">Service</a>
  <a style="left:683px">Contact</a>
</nav>
<div class="abs copy">Copyright © 2010-2023 All rights reserved.</div>

</body>
</html>
```